its a new company based in Christchurch new Zealand building computers ,repairs, upgrades and anything computers for the general public,i like bright happy colours like yellows, greens reds anything that stands out and it needs to communicant trust and security towards my new company,i have no logo yet,

Target Market(s)

target market of all ages

Industry/Entity Type

Building

Contact Information for Business Card

Pixel Harbour Limited,ph-0274829315,email-brightnode47@mailvista.example,14c tamworth cl,kelvale

```html
<!DOCTYPE html>
<html lang="en">
<head>
<meta charset="utf-8">
<title>Pixel Harbour Limited – Business Card</title>
<link rel="stylesheet" href="https://fonts.googleapis.com/css2?family=Exo+2:wght@400;600&family=Saira+Condensed:wght@600&display=swap">
<style>
  :root {
    --canvas-bg: #e4e5e7;
    --card-white: #ffffff;
    --brand-cyan: #1fa8e0;
    --brand-purple: #7d3f98;
    --dark-band: #2f3033;
    --dark-card-top: #3c3d40;
    --dark-card-bottom: #262729;
    --text-grey: #5a5a5a;
    --text-light: #ffffff;
    --shadow: rgba(0,0,0,0.22);
  }
  * { box-sizing: border-box; margin: 0; padding: 0; }
  html, body { width: 1200px; height: 902px; overflow: hidden; }
  body {
    background: var(--canvas-bg);
    font-family: "Exo 2", sans-serif;
    position: relative;
  }
  .card {
    position: absolute;
    left: 290px;
    width: 620px;
    height: 354px;
    border-radius: 4px;
    overflow: hidden;
    box-shadow: 0 12px 30px var(--shadow);
  }
  .card--front { top: 67px; background: var(--card-white); }
  .card--back {
    top: 481px;
    background: linear-gradient(160deg, var(--dark-card-top), var(--dark-card-bottom));
    display: flex; align-items: center; justify-content: center;
  }

  .brand {
    display: flex; align-items: center; gap: 12px;
    color: var(--brand-cyan);
    font-weight: 600;
    line-height: 1.05;
  }
  .brand__mark { width: 16px; height: 16px; background: var(--brand-cyan); flex: none; }
  .brand__name { font-size: 30px; }
  .card--front .brand { position: absolute; left: 34px; top: 40px; }
  .card--back .brand__name { font-size: 32px; }

  .person { position: absolute; left: 300px; top: 66px; width: 290px; }
  .person__name {
    font-family: "Saira Condensed", sans-serif;
    font-weight: 600; font-size: 38px; letter-spacing: 1px;
    color: var(--brand-purple); line-height: 1;
  }
  .person__role {
    font-size: 15px; letter-spacing: 2.5px; color: var(--brand-purple);
    margin-top: 2px;
  }

  .contact-row { display: flex; align-items: center; gap: 7px; font-size: 12px; white-space: nowrap; }
  .icon-box {
    width: 17px; height: 17px; border-radius: 2px; flex: none;
    display: flex; align-items: center; justify-content: center;
  }
  .icon-box svg { width: 11px; height: 11px; }

  .online {
    position: absolute; left: 300px; top: 148px; width: 290px;
    display: flex; flex-direction: column; gap: 7px; color: var(--text-grey);
  }
  .online .icon-box { background: var(--text-grey); }

  .band-blue {
    position: absolute; left: 0; top: 222px; width: 100%; height: 52px;
    background: var(--brand-cyan);
    display: flex; align-items: center; gap: 26px; padding-left: 34px;
    color: var(--text-light);
  }
  .band-blue .icon-box { background: var(--text-light); }

  .band-dark {
    position: absolute; left: 0; top: 274px; width: 100%; height: 80px;
    background: var(--dark-band);
  }
  .pin-box {
    position: absolute; left: 300px; top: 254px;
    width: 36px; height: 36px; border-radius: 3px;
    background: var(--brand-cyan);
    display: flex; align-items: center; justify-content: center;
  }
  .address {
    position: absolute; left: 348px; top: 292px;
    color: var(--text-light); font-size: 15px; line-height: 1.35; letter-spacing: 0.5px;
  }
</style>
</head>
<body>

<section class="card card--front" aria-label="Business card front">
  <div class="brand">
    <span class="brand__mark"></span>
    <span class="brand__name">Pixel Harbour<br>Limited</span>
  </div>

  <div class="person">
    <div class="person__name">ARIA THOMPSON</div>
    <div class="person__role">GENERAL MANAGER</div>
  </div>

  <div class="online">
    <div class="contact-row">
      <span class="icon-box"><svg viewBox="0 0 12 12"><rect x="1" y="2.5" width="10" height="7" fill="none" stroke="#fff" stroke-width="1.2"/><path d="M1 2.5 6 7l5-4.5" fill="none" stroke="#fff" stroke-width="1.2"/></svg></span>
      brightnode47@mailvista.example
    </div>
    <div class="contact-row">
      <span class="icon-box"><svg viewBox="0 0 12 12"><circle cx="6" cy="6" r="4.6" fill="none" stroke="#fff" stroke-width="1.1"/><ellipse cx="6" cy="6" rx="2" ry="4.6" fill="none" stroke="#fff" stroke-width="1"/><path d="M1.4 6h9.2" stroke="#fff" stroke-width="1"/></svg></span>
      www.pixelharbour.example
    </div>
  </div>

  <div class="band-blue">
    <div class="contact-row">
      <span class="icon-box"><svg viewBox="0 0 12 12"><path d="M3 1.5 4.8 3.8 3.8 5a6 6 0 0 0 3.2 3.2l1.2-1 2.3 1.8-1 1.5C6 10.4 1.6 6 1.5 2.5z" fill="#1fa8e0"/></svg></span>
      027 482 9315
    </div>
    <div class="contact-row">
      <span class="icon-box"><svg viewBox="0 0 12 12"><rect x="3" y="1" width="6" height="10" rx="1" fill="none" stroke="#1fa8e0" stroke-width="1.3"/><circle cx="6" cy="9" r="0.8" fill="#1fa8e0"/></svg></span>
      027 482 9315
    </div>
  </div>

  <div class="band-dark"></div>

  <div class="pin-box">
    <svg width="18" height="18" viewBox="0 0 18 18"><path d="M9 1.5a5.5 5.5 0 0 0-5.5 5.5C3.5 11 9 16.5 9 16.5S14.5 11 14.5 7A5.5 5.5 0 0 0 9 1.5z" fill="#fff"/><circle cx="9" cy="7" r="2" fill="#1fa8e0"/></svg>
  </div>
  <div class="address">14c Tamworth Cl,<br>Kelvale</div>
</section>

<section class="card card--back" aria-label="Business card back">
  <div class="brand">
    <span class="brand__mark"></span>
    <span class="brand__name">Pixel Harbour<br>Limited</span>
  </div>
</section>

</body>
</html>
```